Letterhead in Word Template Format

Looking for Modern Elegant Letterhead using our logo and the following information:

218 Wexlow Lane
PO Box 862
Marrow Falls, New York 14210
Phone: (800) 519-4836
Fax: (888) 243-9157
E-Mail: mail@brindleclaimworks.com

Blue adobe code: #3619A8
Orange Adobe code: #F58225

```html
<!DOCTYPE html>
<html lang="en">
<head>
<meta charset="utf-8">
<title>Brindle Claimworks Letterhead</title>
<link href="https://fonts.googleapis.com/css2?family=Montserrat:ital,wght@0,400;0,600;0,700;0,800;1,400&display=swap" rel="stylesheet">
<style>
  :root {
    --brand-blue: #3619A8;
    --brand-orange: #F58225;
    --ink: #444444;
    --paper: #ffffff;
    --backdrop: #ece9e4;
    --signature-tone: #e4e4e4;
  }
  * { margin: 0; padding: 0; box-sizing: border-box; }
  html, body {
    width: 1200px; height: 1200px; overflow: hidden;
    background: var(--backdrop);
    font-family: "Montserrat", sans-serif;
    color: var(--ink);
  }
  .letterhead {
    position: absolute; left: 167px; top: 40px;
    width: 866px; height: 1120px;
    background: var(--paper);
  }
  .top-band { position: absolute; left: 0; top: 0; }
  .brand {
    position: absolute; left: 71px; top: 70px;
    font-size: 30px; font-weight: 800; color: var(--brand-orange);
    line-height: 40px; white-space: nowrap;
  }
  .letter-date {
    position: absolute; right: 175px; top: 201px;
    font-size: 15px; font-weight: 700; line-height: 20px;
  }
  .recipient { position: absolute; left: 157px; top: 252px; font-size: 15.4px; line-height: 21.5px; }
  .recipient-name { font-weight: 700; }
  .recipient-role { font-style: italic; margin-bottom: 4px; }
  .contact-row { display: flex; }
  .contact-key { width: 24px; }
  .letter-body { position: absolute; left: 157px; top: 427px; width: 548px; }
  .letter-body p { font-size: 15.4px; line-height: 23.6px; margin-bottom: 20px; }
  .closing {
    position: absolute; left: 541px; top: 833px; width: 180px;
    text-align: center; font-size: 15.4px; line-height: 20px;
  }
  .closing-phrase { text-align: right; padding-right: 30px; }
  .signature-area {
    width: 146px; height: 46px; margin: 3px 0 5px 23px;
    background: var(--signature-tone); border-radius: 4px;
  }
  .signer-name { font-weight: 700; text-align: center; }
  .footer { position: absolute; left: 99px; top: 1019px; width: 668px; height: 70px; }
  .footer-rule { position: absolute; left: 0; right: 0; top: 13px; height: 1px; background: var(--brand-orange); }
  .footer-icon { position: absolute; top: 0; width: 26px; height: 26px; }
  .footer-text { position: absolute; top: 29px; font-size: 9.6px; line-height: 15px; white-space: nowrap; color: #333; }
</style>
</head>
<body>
<main class="letterhead">
  <svg class="top-band" width="866" height="28" viewBox="0 0 866 28">
    <path d="M0 0 H358 C372 1 381 5 386 9 H0 Z" fill="var(--brand-blue)"/>
    <path d="M366 0 H866 V27 H418 C398 27 394 4 366 0 Z" fill="var(--brand-orange)"/>
  </svg>

  <header class="brand">BRINDLE CLAIMWORKS</header>

  <div class="letter-date">Date, 01 April 2021</div>

  <section class="recipient">
    <div>To:</div>
    <div class="recipient-name">Daniel Hart</div>
    <div class="recipient-role">Chief Officer</div>
    <div class="contact-row"><span class="contact-key">A</span><span>: Stret address goes here</span></div>
    <div class="contact-row"><span class="contact-key">W</span><span>: www.danielhart.com</span></div>
    <div class="contact-row"><span class="contact-key">P</span><span>: +123 456 789 10</span></div>
  </section>

  <article class="letter-body">
    <p>Lorem ipsum dolor sit amet, consectetur adipiscing elit. Duis auctor sem vel metus interdum porta. Duis consequat bibendum felis eget cursus. Nulla eget purus vehicula ipsum finibus egestas. Nullam ligula ipsum, mollis sed gravida vitae, maximus eu dolor. Morbi luctus sem a congue consectetur.</p>
    <p>Orci varius natoque penatibus et magnis dis parturient montes, nascetur ridiculus mus. Vestibulum congue eros auctor, ullamcorper libero blandit, tempor tellus. Proin vitae tellus et nunc fringilla lacinia. Sed augue erat, facilisis laoreet velit a, convallis mattis nunc. Nunc sagittis ligula vitae sollicitudin sollicitudin.</p>
    <p>Nulla facilisi. Nulla quis odio vitae purus aliquam fermentum ut nec diam. Fusce sed velit ultrices, aliquam augue ut, sollicitudin orci. Quisque in gravida urna. Curabitur id purus odio. Suspendisse potenti. Nunc dictum vel sapien a vestibulum.</p>
  </article>

  <section class="closing">
    <div class="closing-phrase">Kind Regards</div>
    <div class="signature-area" role="img" aria-label="Handwritten signature of the sender"></div>
    <div class="signer-name">Daniel Hart</div>
  </section>

  <footer class="footer">
    <div class="footer-rule"></div>

    <svg class="footer-icon" style="left:57px" viewBox="0 0 26 26">
      <circle cx="13" cy="13" r="13" fill="var(--brand-orange)"/>
      <path d="M13 5.5c-3 0-5.2 2.3-5.2 5.1 0 3.6 5.2 9.4 5.2 9.4s5.2-5.8 5.2-9.4c0-2.8-2.2-5.1-5.2-5.1z" fill="#fff"/>
      <circle cx="13" cy="10.6" r="2" fill="var(--brand-orange)"/>
    </svg>
    <svg class="footer-icon" style="left:252px" viewBox="0 0 26 26">
      <circle cx="13" cy="13" r="13" fill="var(--brand-orange)"/>
      <path d="M9 6.5l2.3 0 1.2 3.3-1.6 1.2c.8 1.8 2.2 3.2 4 4l1.2-1.6 3.3 1.2v2.3c0 .9-.8 1.6-1.7 1.5C11.6 17.9 8 14.3 7.6 8.2 7.5 7.3 8.1 6.5 9 6.5z" fill="#fff"/>
    </svg>
    <svg class="footer-icon" style="left:411px" viewBox="0 0 26 26">
      <circle cx="13" cy="13" r="13" fill="var(--brand-orange)"/>
      <rect x="7" y="9" width="12" height="10" rx="1.2" fill="#fff"/>
      <rect x="9.5" y="5.5" width="7" height="5" fill="#fff" stroke="var(--brand-orange)" stroke-width="1"/>
      <rect x="9" y="12" width="2.6" height="5" fill="var(--brand-orange)"/>
      <circle cx="14.5" cy="13" r=".9" fill="var(--brand-orange)"/>
      <circle cx="16.8" cy="13" r=".9" fill="var(--brand-orange)"/>
      <circle cx="14.5" cy="15.8" r=".9" fill="var(--brand-orange)"/>
      <circle cx="16.8" cy="15.8" r=".9" fill="var(--brand-orange)"/>
    </svg>
    <svg class="footer-icon" style="left:590px" viewBox="0 0 26 26">
      <circle cx="13" cy="13" r="13" fill="var(--brand-orange)"/>
      <path d="M6 12.5L19.5 7 16 19.5l-3.5-3.3-2 2v-3.4l6-6.3-7.4 5.2z" fill="#fff"/>
    </svg>

    <div class="footer-text" style="left:0">218 Wexlow Lane&nbsp; PO Box 862<br>Marrow Falls, New York 14210</div>
    <div class="footer-text" style="left:265px; transform:translateX(-50%)">(800) 519-4836</div>
    <div class="footer-text" style="left:424px; transform:translateX(-50%)">(888) 243-9157</div>
    <div class="footer-text" style="right:0">mail@brindleclaimworks.com</div>
  </footer>
</main>
</body>
</html>
```